Professional Package for CPA Firm

We would like a stationery design for our new CPA Firm based in Atlanta, GA called 'Vale 7'. We work with investors to help grow investments, tax free. We would like the design to have a professional/minimal look with a 'wow' factor. We need 9.5″ x 4.125″, 9x12, and 10x13 mailing envelopes, business cards, and a letterhead. We have a logo that is already complete. For the letterhead, we would like to have space to put credentials at the bottom of the page

Industry/Entity Type

CPA, Accounting

```html
<!DOCTYPE html>
<html lang="en">
<head>
<meta charset="utf-8">
<title>Vale 7 — Stationery</title>
<link rel="stylesheet" href="https://fonts.googleapis.com/css2?family=Montserrat:wght@400;500;800&family=Open+Sans:wght@400;600&family=Roboto:ital,wght@0,400;1,400&display=swap">
<style>
  :root {
    --bg: #e4e4e4;
    --paper: #efefef;
    --paper-edge: #dcdcdc;
    --ink: #1c1c1c;
    --body: #4a4a4a;
    --blue: #2a93cc;
    --blue-deep: #1d86c2;
    --photo-light: #d7dce0;
    --photo-mid: #9aa3ad;
    --photo-dark: #3b4350;
    --shade: rgba(40,40,40,0.72);
  }
  * { box-sizing: border-box; margin: 0; padding: 0; }
  html, body { width: 1200px; height: 795px; overflow: hidden; background: var(--bg); }
  .canvas { position: relative; width: 1200px; height: 795px; }

  .sheet {
    position: absolute; background: var(--paper);
    box-shadow: 0 1px 3px rgba(0,0,0,0.12);
  }

  /* Wordmark */
  .brand { display: flex; flex-direction: column; align-items: center; font-family: "Montserrat", sans-serif; color: var(--ink); }
  .brand-row { display: flex; align-items: center; }
  .brand-square { background: var(--blue); display: inline-block; }
  .brand-name { font-weight: 800; line-height: 1; letter-spacing: 0.02em; }
  .brand-tag { font-weight: 500; letter-spacing: 0.08em; line-height: 1.2; }

  /* Letterhead */
  .letterhead { left: 292px; top: 99px; width: 293px; height: 415px; }
  .letterhead .brand { position: absolute; left: 0; right: 0; top: 56px; }
  .letterhead .brand-square { width: 13px; height: 13px; margin-right: 5px; }
  .letterhead .brand-name { font-size: 16px; }
  .letterhead .brand-tag { font-size: 4.6px; margin-top: 2px; }
  .letter-body {
    position: absolute; left: 26px; right: 26px; top: 97px;
    font-family: "Open Sans", sans-serif; font-size: 5.4px; line-height: 8px; color: var(--body);
  }
  .letter-body p { text-align: justify; margin-bottom: 8px; }
  .letter-body .salute { margin-bottom: 7px; }
  .signature-space { width: 34px; height: 30px; background: #e7e7e7; margin-top: -2px; }
  .letter-footer {
    position: absolute; left: 0; right: 0; top: 371px; text-align: center;
    font-family: "Roboto", sans-serif; font-size: 5.4px; line-height: 8px; color: #555;
  }
  .letter-footer .contact-line { display: flex; justify-content: center; align-items: center; gap: 3px; }
  .letter-footer svg { width: 5px; height: 5px; fill: #333; }
  .letter-footer .credentials { font-style: italic; }

  /* Folder */
  .folder { left: 637px; top: 80px; width: 346px; height: 437px; }
  .folder .spine { position: absolute; top: 0; bottom: 0; width: 1px; background: var(--paper-edge); }
  .folder .photo-band { position: absolute; left: 0; top: 95px; width: 346px; height: 225px; }
  .folder .brand { position: absolute; right: 20px; top: 361px; }
  .folder .brand-square { width: 13px; height: 13px; margin-right: 5px; }
  .folder .brand-name { font-size: 16px; }
  .folder .brand-tag { font-size: 4.6px; margin-top: 2px; }

  /* Business cards */
  .card { width: 132px; height: 75px; }
  .card-front { left: 187px; top: 551px; display: flex; align-items: center; }
  .card-front .brand { width: 62px; }
  .card-front .brand-square { width: 7px; height: 7px; margin-right: 3px; }
  .card-front .brand-name { font-size: 9px; }
  .card-front .brand-tag { font-size: 2.6px; margin-top: 1px; }
  .card-divider { width: 1px; height: 34px; background: var(--blue); margin: 0 6px 0 4px; }
  .card-details { font-family: "Roboto", sans-serif; font-size: 2.9px; line-height: 4.4px; color: var(--ink); }
  .card-details .person { font-family: "Montserrat", sans-serif; font-weight: 800; font-size: 3.8px; line-height: 4.4px; }
  .card-details .role { margin-bottom: 2px; }
  .card-details .detail { display: flex; align-items: center; gap: 1.5px; }
  .card-details svg { width: 3px; height: 3px; fill: var(--ink); }
  .card-back { left: 187px; top: 647px; display: flex; align-items: center; justify-content: center; }
  .card-back .brand-square { width: 11px; height: 11px; margin-right: 4px; }
  .card-back .brand-name { font-size: 14px; }
  .card-back .brand-tag { font-size: 4px; margin-top: 1.5px; }

  /* Envelopes */
  .envelope { width: 329px; height: 157px; top: 561px; }
  .envelope-front { left: 353px; }
  .envelope-front .return-block { position: absolute; left: 22px; top: 24px; }
  .envelope-front .brand-square { width: 13px; height: 13px; margin-right: 5px; }
  .envelope-front .brand-name { font-size: 15px; }
  .envelope-front .brand-tag { font-size: 4.4px; margin-top: 2px; }
  .envelope-front .return-address { font-family: "Roboto", sans-serif; font-size: 5px; line-height: 6px; color: #444; text-align: center; margin-top: 2px; }
  .envelope-back { left: 714px; }
  .envelope-back .flap { position: absolute; left: 0; top: 0; width: 329px; height: 56px; }
  .envelope-back .brand { position: absolute; left: 0; right: 0; top: 20px; }
  .envelope-back .brand-square { width: 7px; height: 7px; margin-right: 3px; }
  .envelope-back .brand-name { font-size: 9px; }
  .envelope-back .brand-tag { font-size: 2.6px; margin-top: 1px; }
</style>
</head>
<body>
<main class="canvas">

  <!-- Letterhead -->
  <section class="sheet letterhead">
    <div class="brand">
      <div class="brand-row"><span class="brand-square"></span><span class="brand-name">VALE 7</span></div>
      <div class="brand-tag">CPAs and Tax Advisors</div>
    </div>
    <div class="letter-body">
      <p class="salute">Dear customer,</p>
      <p>Lorem ipsum dolor sit amet, consectetur adipisicing elit, sed do eiusmod tempor incididunt ut labore et dolore magna aliqua. Ut enim ad minim veniam, quis nostrud exercitation ullamco laboris nisi ut aliquip ex ea commodo consequat. Duis aute irure dolor in reprehenderit in voluptate velit esse cillum dolore eu fugiat nulla pariatur. Excepteur sint occaecat cupidatat non proident, sunt in culpa qui officia deserunt mollit anim id est laborum.</p>
      <p>Lorem ipsum dolor sit amet, consectetur adipisicing elit, sed do eiusmod tempor incididunt ut labore et dolore magna aliqua. Ut enim ad minim veniam, quis nostrud exercitation ullamco laboris nisi ut aliquip ex ea commodo consequat. Duis aute irure dolor in reprehenderit in voluptate velit esse cillum dolore eu fugiat nulla pariatur. Excepteur sint occaecat cupidatat non proident, sunt in culpa qui officia deserunt mollit anim id est laborum.</p>
      <p>Lorem ipsum dolor sit amet, consectetur adipisicing elit, sed do eiusmod tempor incididunt ut labore et dolore magna aliqua. Ut enim ad minim veniam, quis nostrud exercitation ullamco laboris nisi ut aliquip ex ea commodo consequat. Duis aute irure dolor in reprehenderit in voluptate velit esse cillum dolore eu fugiat nulla pariatur. Excepteur sint occaecat cupidatat non proident, sunt in culpa qui officia deserunt mollit anim id est laborum.</p>
      <p>Lorem ipsum dolor sit amet, consectetur adipisicing elit, sed do eiusmod tempor incididunt ut labore et dolore magna aliqua. Ut enim ad minim veniam, quis nostrud exercitation ullamco laboris nisi ut aliquip ex ea commodo consequat. Duis aute irure dolor in reprehenderit.</p>
      <p class="salute">Yours Sincerely,</p>
      <div class="signature-space" role="img" aria-label="Handwritten signature"></div>
    </div>
    <footer class="letter-footer">
      <div>2280 Cedar Lane, Suite 210, Atlanta, GA 30318</div>
      <div class="contact-line">
        <svg viewBox="0 0 10 10"><path d="M2 0.5 L3.8 2.6 L2.8 3.8 Q4 6 6.2 7.2 L7.4 6.2 L9.5 8 L8.2 9.5 Q4.5 9.5 0.5 4.5 Q0.5 1.8 2 0.5Z"/></svg>
        <span>404-555-0172</span>
        <svg viewBox="0 0 10 10"><path d="M0 2h10v6H0z M0.8 2.6 L5 5.6 L9.2 2.6" fill="#333"/><path d="M0.8 2.6 L5 5.6 L9.2 2.6" stroke="#fff" stroke-width="0.8" fill="none"/></svg>
        <span>team@vale7cpas.com</span>
        <svg viewBox="0 0 10 10"><circle cx="5" cy="5" r="4.3" fill="none" stroke="#333" stroke-width="1"/><path d="M0.7 5h8.6M5 0.7v8.6" stroke="#333" stroke-width="0.8"/></svg>
        <span>www.vale7cpas.com</span>
      </div>
      <div class="credentials">Member of the Southeast Society and National Institute of CPAs</div>
    </footer>
  </section>

  <!-- Presentation folder -->
  <section class="sheet folder">
    <span class="spine" style="left:7px"></span>
    <span class="spine" style="left:20px"></span>
    <svg class="photo-band" viewBox="0 0 346 225" aria-hidden="false">
      <defs>
        <linearGradient id="meetingTones" x1="0" y1="0" x2="0" y2="1">
          <stop offset="0" stop-color="var(--photo-light)"/>
          <stop offset="0.55" stop-color="var(--photo-mid)"/>
          <stop offset="1" stop-color="var(--photo-dark)"/>
        </linearGradient>
      </defs>
      <rect width="346" height="225" fill="url(#meetingTones)" role="img" aria-label="Photo of a team of advisors meeting around an office table"/>
      <polygon points="0,18 0,225 92,225" fill="var(--shade)"/>
      <polygon points="251,0 346,0 346,172 312,172" fill="var(--blue-deep)" opacity="0.92"/>
    </svg>
    <div class="brand">
      <div class="brand-row"><span class="brand-square"></span><span class="brand-name">VALE 7</span></div>
      <div class="brand-tag">CPAs and Tax Advisors</div>
    </div>
  </section>

  <!-- Business card, front -->
  <section class="sheet card card-front">
    <div class="brand">
      <div class="brand-row"><span class="brand-square"></span><span class="brand-name">VALE 7</span></div>
      <div class="brand-tag">CPAs and Tax Advisors</div>
    </div>
    <span class="card-divider"></span>
    <div class="card-details">
      <div class="person">NOAH BRANDT, CPA</div>
      <div class="role">Managing Partner</div>
      <div>2280 Cedar Lane, Suite</div>
      <div>210, Atlanta, GA 30318</div>
      <div class="detail"><svg viewBox="0 0 10 10"><path d="M2 0.5 L3.8 2.6 L2.8 3.8 Q4 6 6.2 7.2 L7.4 6.2 L9.5 8 L8.2 9.5 Q4.5 9.5 0.5 4.5 Q0.5 1.8 2 0.5Z"/></svg>404-555-0172</div>
      <div class="detail"><svg viewBox="0 0 10 10"><path d="M0 2h10v6H0z"/></svg>nbrandt@vale7cpas.com</div>
      <div class="detail"><svg viewBox="0 0 10 10"><circle cx="5" cy="5" r="4.3" fill="none" stroke="#1c1c1c" stroke-width="1.2"/></svg>www.vale7cpas.com</div>
    </div>
  </section>

  <!-- Business card, back -->
  <section class="sheet card card-back">
    <div class="brand">
      <div class="brand-row"><span class="brand-square"></span><span class="brand-name">VALE 7</span></div>
      <div class="brand-tag">CPAs and Tax Advisors</div>
    </div>
  </section>

  <!-- Envelope, front -->
  <section class="sheet envelope envelope-front">
    <div class="return-block">
      <div class="brand">
        <div class="brand-row"><span class="brand-square"></span><span class="brand-name">VALE 7</span></div>
        <div class="brand-tag">CPAs and Tax Advisors</div>
      </div>
      <div class="return-address">2280 Cedar Lane, Suite<br>210, Atlanta, GA 30318</div>
    </div>
  </section>

  <!-- Envelope, back -->
  <section class="sheet envelope envelope-back">
    <svg class="flap" viewBox="0 0 329 56" aria-hidden="true">
      <path d="M1 3 L7 54 L322 54 L328 3" fill="none" stroke="#d6d6d6" stroke-width="0.8"/>
    </svg>
    <div class="brand">
      <div class="brand-row"><span class="brand-square"></span><span class="brand-name">VALE 7</span></div>
      <div class="brand-tag">CPAs and Tax Advisors</div>
    </div>
  </section>

</main>
</body>
</html>
```